Website Design for Horse Blog
Purely Brivelle
Project: Website Design for Horse Blog
Website Design for Horse Blog - Blogging
Creative Brief
Blogging
Brivelle Saddlebreds is a boutique saddlebred horse breeding operation. Purely Brivelle is the name of the blog encouraging older people that it is never too late to start riding horses. It's a feel-good blog intended to attract more people to the Saddlebred Horse Showing industry.
Simple, user-friendly without too much going on. Photography is important.
Modern
Burgundy
Black
Ivory
left side
http://joannevrelstad.example
Most importantly I want to set this website for blogging purposes. The business is just an example of what it is I do. Links to resources will be important for a page. I'm thinking five pages: Blog/Brivelle Saddlebreds/For Sale/Links/Contact Info
crewdalvo crewdalvo
Here is my revised requests: Five pages should be: Home, Blog, Brivelle Saddlebreds, Contact, Links. The title: Purely Brivelle should appear on the Home page along with the Brivelle Saddlebreds logo. I like simple, modern looking pages without a lot of information hitting me from every direction. I have seen very few with black backgrounds, I would like to see more of that.
I think I would like to see the title Purely Brivelle to be displayed with more emphasis as soon as the page loads.

```html
<!DOCTYPE html>
<html lang="en">
<head>
<meta charset="utf-8">
<title>Purely Brivelle</title>
<link rel="stylesheet" href="https://fonts.googleapis.com/css2?family=Open+Sans:wght@400;600;700&family=Great+Vibes&display=swap">
<style>
:root{
  --burgundy:#7a1626;
  --burgundy-deep:#5a0f1b;
  --rose:#b9797f;
  --salmon:#d9867d;
  --ivory:#fbf7f0;
  --gold:#f6cf6a;
  --ink:#2a1a14;
  --footer:rgba(40,40,34,.88);
}
*{margin:0;padding:0;box-sizing:border-box}
html,body{width:1200px;height:1078px;overflow:hidden}
body{font-family:"Open Sans",Arial,sans-serif;background:#6b6a58;position:relative}
.backdrop{position:absolute;inset:0;
  background:
    linear-gradient(180deg,#efe9e6 0%,#e2dcd8 22%,#b2ab9a 48%,#6f6d4f 68%,#5c6043 84%,#3d3f30 100%);}
.topbar{position:absolute;left:0;top:0;width:1200px;height:80px}
.contact{position:absolute;left:110px;top:24px;display:flex;align-items:flex-start;gap:18px}
.contact svg{margin-top:8px}
.contact p{font-size:13px;font-weight:700;color:var(--burgundy-deep);line-height:19px}
.social{position:absolute;left:950px;top:26px;display:flex;gap:10px}
.social span{width:29px;height:29px;border-radius:3px;display:block}
.social .s1{background:#3b5a98}.social .s2{background:#2aa4dc}
.social .s3{background:#f2891f}.social .s4{background:#d74532}
.stage{position:absolute;left:102px;top:82px;width:999px;height:751px;overflow:hidden;box-shadow:0 2px 12px rgba(0,0,0,.25)}
.hero-photo{position:absolute;inset:0;
  background:linear-gradient(180deg,#dfe2e6 0%,#c9ccd0 40%,#8a6a4c 52%,#6f8c4a 72%,#4d7035 100%)}
.sidebar{position:absolute;left:0;top:0;width:335px;height:751px;
  background:linear-gradient(180deg,rgba(170,90,105,.72) 0%,rgba(150,70,85,.72) 60%,rgba(160,80,95,.6) 100%)}
.brand{position:absolute;left:0;top:0;width:335px;height:166px;background:var(--ivory);
  clip-path:polygon(0 0,100% 0,92% 100%,0 100%);text-align:center;padding-top:40px}
.brand-mark{display:inline-flex;align-items:center;gap:10px;font-size:30px;font-weight:700;color:var(--burgundy)}
.brand-mark i{width:22px;height:22px;border-radius:50%;background:var(--burgundy);display:block}
.brand-title{margin-top:14px;font-size:15px;font-weight:600;letter-spacing:2px;color:var(--salmon);text-transform:uppercase}
.nav{position:absolute;left:58px;top:193px;list-style:none}
.nav li{height:61px;font-size:14px;font-weight:700;color:#fff;text-transform:uppercase;letter-spacing:.3px}
.quote{position:absolute;left:44px;top:515px;width:154px;height:44px;background:var(--gold);
  color:var(--ink);font-size:14px;font-weight:700;text-transform:uppercase;display:flex;align-items:center;justify-content:center}
.emblem{position:absolute;left:40px;top:640px;width:90px;height:90px;border-radius:50%;border:3px solid rgba(255,255,255,.25)}
.slider-dots{position:absolute;left:451px;top:725px;width:102px;height:26px;background:var(--burgundy);
  display:flex;align-items:center;justify-content:center;gap:14px}
.slider-dots span{width:8px;height:8px;border-radius:50%;background:#fff;opacity:.7}
.slider-dots span.on{opacity:1}
.tagline{position:absolute;left:80px;top:860px;width:1040px;text-align:center;
  font-family:"Great Vibes",cursive;font-size:31px;line-height:59px;color:#fff;text-shadow:0 1px 3px rgba(0,0,0,.35)}
.footer{position:absolute;left:0;top:1011px;width:1200px;height:67px;background:var(--footer);
  display:flex;align-items:center;justify-content:center;font-size:12px;color:#eee}
</style>
</head>
<body>
<div class="backdrop" role="img" aria-label="Soft blurred photograph of horses beside a paddock fence"></div>

<header class="topbar">
  <div class="contact">
    <svg width="26" height="18" viewBox="0 0 26 18" aria-hidden="true">
      <rect x="1" y="1" width="24" height="16" fill="var(--burgundy-deep)"/>
      <path d="M1 1 L13 10 L25 1" fill="none" stroke="#efe9e6" stroke-width="2"/>
    </svg>
    <p>info@brivellestable.example<br>(555) - 0142 - 7731</p>
  </div>
  <div class="social" aria-label="Social links">
    <span class="s1"></span><span class="s2"></span><span class="s3"></span><span class="s4"></span>
  </div>
</header>

<main class="stage">
  <div class="hero-photo" role="img" aria-label="Rider standing between two chestnut saddlebred horses in a fenced green paddock"></div>
  <aside class="sidebar">
    <div class="brand">
      <div class="brand-mark"><i></i>Brivelle</div>
      <div class="brand-title">Purely Brivelle</div>
    </div>
    <ul class="nav">
      <li>Home</li>
      <li>Blog</li>
      <li>Brivelle Saddlebreds</li>
      <li>For Sale</li>
      <li>Links/Contact</li>
    </ul>
    <div class="quote">Get a Quote</div>
    <div class="emblem" aria-hidden="true"></div>
  </aside>
  <div class="slider-dots"><span class="on"></span><span></span><span></span></div>
</main>

<p class="tagline">Brivelle Saddlebreds is a boutique saddlebred horse breeding operation. Purely Brivelle is the name of the blog encouraging older people that it is never too late to start riding horses.</p>

<footer class="footer">All Rights Reserved . Copyright©2015@brivellestable.example</footer>
</body>
</html>
```